Family Ranch with a hobby vineyard needs 2 wine labels for our first harvest

Design 2 wine labels (front and back) with the Brindor Ranch logo.
Label 1:
Sauvignon Blanc
Alc. 12.5% by Vol.
Palos Verdes Peninsula - add as the region
Year 2022
Label 2:
Cabernet Sauvignon
Alc. 13.5% by Vol.
Year 2022
For the back label design:
GOVERNMENT WARNING: (1) According to the Surgeon General, women
should not drink alcoholic beverages during pregnancy because of the risk of
birth defects. (2) Consumption of alcoholic beverages impairs your ability to
drive a car or operate machinery, and may cause health problems.
Contains Sulfates.
750ML
I just received the bottles and have attached a picture.
Look and feel
Each slider illustrates characteristics of the customer's brand and the style your logo design should communicate.

```html
<!DOCTYPE html>
<html lang="en">
<head>
<meta charset="utf-8">
<title>Brindor Ranch – Cabernet Sauvignon 2022 Label</title>
<link rel="stylesheet" href="https://fonts.googleapis.com/css2?family=Josefin+Sans:wght@300;400&family=Kaushan+Script&family=Montserrat:wght@600&family=Old+Standard+TT:wght@400;700&display=swap">
<style>
  :root {
    --backdrop: #0e0e0e;
    --label-paper: #ebe8da;
    --label-edge: #d9d5c4;
    --ribbon-tone: #dedac9;
    --ribbon-tone-deep: #d3cebb;
    --ink: #1e1e1e;
    --ink-soft: #2e2e2c;
    --gold: #a8893e;
  }
  * { margin: 0; padding: 0; box-sizing: border-box; }
  html, body {
    width: 1200px;
    height: 800px;
    overflow: hidden;
    background: var(--backdrop);
  }
  .canvas {
    width: 1200px;
    height: 800px;
    display: flex;
    align-items: center;
    justify-content: center;
  }
  .wine-label {
    width: 580px;
    height: 740px;
    background: var(--label-paper);
    border: 1px solid var(--label-edge);
    display: flex;
    flex-direction: column;
    align-items: center;
    padding: 70px 0 64px;
    color: var(--ink);
  }
  .region {
    position: relative;
    width: 420px;
    height: 64px;
    display: flex;
    align-items: center;
    justify-content: center;
  }
  .region-ribbon {
    position: absolute;
    inset: 0;
    background: linear-gradient(180deg, var(--ribbon-tone), var(--ribbon-tone-deep));
  }
  .region-name {
    position: relative;
    font-family: "Josefin Sans", sans-serif;
    font-weight: 300;
    font-size: 26px;
    letter-spacing: 6px;
    padding-left: 6px;
    color: var(--ink);
  }
  .region-sub {
    font-family: "Kaushan Script", cursive;
    font-size: 40px;
    line-height: 1.2;
    margin-top: 10px;
    color: var(--ink);
  }
  .brand {
    margin-top: 40px;
    display: flex;
    flex-direction: column;
    align-items: center;
    gap: 26px;
  }
  .brand-dot {
    width: 66px;
    height: 66px;
    border-radius: 50%;
    border: 5px solid var(--gold);
  }
  .brand-name {
    font-family: "Montserrat", sans-serif;
    font-weight: 600;
    font-size: 46px;
    line-height: 1;
    letter-spacing: 4px;
    text-transform: uppercase;
    color: var(--ink);
  }
  .varietal {
    margin-top: auto;
    font-family: "Old Standard TT", serif;
    font-weight: 400;
    font-size: 32px;
    letter-spacing: 1px;
    color: var(--ink);
  }
  .vintage {
    margin-top: 12px;
    font-family: "Old Standard TT", serif;
    font-weight: 700;
    font-size: 36px;
    color: var(--ink);
  }
  .abv {
    margin-top: 30px;
    font-family: "Old Standard TT", serif;
    font-weight: 700;
    font-size: 24px;
    color: var(--ink-soft);
  }
</style>
</head>
<body>
<main class="canvas">
  <article class="wine-label">
    <div class="region">
      <div class="region-ribbon" role="img" aria-label="Ribbon banner ornament framing the region name"></div>
      <p class="region-name">PALOS VERDES</p>
    </div>
    <p class="region-sub">Peninsula</p>
    <div class="brand">
      <span class="brand-dot"></span>
      <h1 class="brand-name">Brindor Ranch</h1>
    </div>
    <p class="varietal">CABERNET SAUVIGNON</p>
    <p class="vintage">2022</p>
    <p class="abv">Alc. 13.5% by Vol.</p>
  </article>
</main>
</body>
</html>
```